Steady Harbour Coaching Business Card

We need a business card for a new business based in Sydney Australia called "Steady Harbour Coaching". The business provides the following:
1. Resilience systems for individuals - Developing personalised resilience programs that increase stress tolerance, improve work effectiveness and minimise stress responses to challenge.
2. Group Resilience Training for Leaders and managers - Delivering Resilience training packages and ongoing support to leadership cadres within organisations.
3. High Risk Resilience Training - providing resilience training for High Risk professions such as emergency responders, military and police.

Target Market(s)

Corporate / Military / Emergency Responders

Industry/Entity Type

Leadership

Contact Information for Business Card

Steady Harbour Coaching, Derek Falwood, 7/19 Kestrel St Penbrook 2093, quiet.morning.tide@mailpost.example, www.steadyharbourcoaching.example.au, M# 0417603842
Tailored Calm Under Pressure Programs for managers and frontline service crews

Requirements
Must have
• 1. Creation of a logo/graphic - to include 3 elements:
a. Military
b.Corporate
c. Emergency Responder.

As long as those 3 elements are included - I am open to any potential designs. Preference given to those who can create a logo out of the above three elements.

```html
<!DOCTYPE html>
<html lang="en">
<head>
<meta charset="utf-8">
<title>Steady Harbour Coaching – Business Card</title>
<link rel="stylesheet" href="https://fonts.googleapis.com/css2?family=Roboto:wght@400;700&display=swap">
<style>
  :root {
    --backdrop-light: #c9c9c9;
    --backdrop-dark: #6e6e6e;
    --card-black: #0c0c0c;
    --card-panel: #1a1a1a;
    --accent-orange: #f07a3a;
    --accent-orange-deep: #e0662a;
    --text-orange: #f28a4e;
  }
  * { margin: 0; padding: 0; box-sizing: border-box; }
  html, body {
    width: 1200px;
    height: 1023px;
    overflow: hidden;
  }
  body {
    background: radial-gradient(ellipse at 50% 30%, var(--backdrop-light) 0%, var(--backdrop-dark) 100%);
    font-family: "Roboto", Arial, sans-serif;
    position: relative;
  }
  .business-card {
    position: absolute;
    left: 100px;
    top: 226px;
    width: 1000px;
    height: 571px;
    background: var(--card-black);
    border-radius: 6px;
    overflow: hidden;
    box-shadow: 0 24px 50px rgba(0, 0, 0, 0.45);
  }
  .card-lines {
    position: absolute;
    inset: 0;
  }
  .emblem-artwork {
    position: absolute;
    left: 40px;
    top: 140px;
    width: 230px;
    height: 230px;
    border-radius: 50%;
    background: radial-gradient(circle at 45% 40%, var(--accent-orange) 0%, var(--accent-orange-deep) 100%);
  }
  .brand-name {
    position: absolute;
    left: 470px;
    top: 34px;
    color: var(--accent-orange);
    font-weight: 700;
    line-height: 1;
  }
  .brand-name .brand-top {
    display: block;
    font-size: 34px;
    letter-spacing: 1px;
  }
  .brand-name .brand-main {
    display: block;
    font-size: 104px;
    margin-top: 2px;
  }
  .holder-name {
    position: absolute;
    left: 52px;
    top: 405px;
    font-size: 40px;
    font-weight: 700;
    color: var(--text-orange);
  }
  .contact-list {
    position: absolute;
    list-style: none;
    color: var(--text-orange);
    font-size: 21px;
  }
  .contact-list li {
    display: flex;
    align-items: center;
    gap: 10px;
    height: 30px;
  }
  .contact-list svg {
    width: 16px;
    height: 16px;
    flex: none;
  }
  .contact-personal { left: 52px; top: 456px; }
  .contact-business { left: 560px; top: 218px; }
  .tagline {
    position: absolute;
    left: 52px;
    top: 528px;
    font-size: 22px;
    color: var(--text-orange);
    white-space: nowrap;
  }
</style>
</head>
<body>
  <div class="business-card">
    <svg class="card-lines" width="1000" height="571" viewBox="0 0 1000 571" aria-hidden="true">
      <path d="M0 395 L300 395 L455 195 L1000 195 L1000 520 L0 520 Z" fill="var(--card-panel)"/>
      <path d="M0 395 L300 395 L455 195 L1000 195" fill="none" stroke="var(--accent-orange)" stroke-width="4"/>
      <line x1="0" y1="520" x2="1000" y2="520" stroke="var(--accent-orange)" stroke-width="2"/>
    </svg>

    <div class="emblem-artwork" role="img" aria-label="Orange sun disc with dark silhouettes of a soldier, an office worker and a firefighter standing together"></div>

    <h1 class="brand-name">
      <span class="brand-top">STEADY HARBOUR</span>
      <span class="brand-main">Coaching</span>
    </h1>

    <ul class="contact-list contact-business">
      <li>
        <svg viewBox="0 0 16 16" aria-hidden="true"><path d="M8 1 L15 8 H13 V15 H3 V8 H1 Z" fill="var(--text-orange)"/></svg>
        7/19 Kestrel St Penbrook 2093
      </li>
      <li>
        <svg viewBox="0 0 16 16" aria-hidden="true"><circle cx="8" cy="8" r="7" fill="var(--text-orange)"/><path d="M1 8 H15 M8 1 C4 5 4 11 8 15 M8 1 C12 5 12 11 8 15" stroke="var(--card-black)" stroke-width="1" fill="none"/></svg>
        www.steadyharbourcoaching.example.au
      </li>
    </ul>

    <h2 class="holder-name">Derek Falwood</h2>

    <ul class="contact-list contact-personal">
      <li>
        <svg viewBox="0 0 16 16" aria-hidden="true"><path d="M4 1 L7 4 L5 6 C6 8 8 10 10 11 L12 9 L15 12 L12 15 C6 14 2 10 1 4 Z" fill="var(--text-orange)"/></svg>
        0417603842
      </li>
      <li>
        <svg viewBox="0 0 16 16" aria-hidden="true"><rect x="1" y="3" width="14" height="10" fill="var(--text-orange)"/><path d="M1 3 L8 9 L15 3" stroke="var(--card-black)" stroke-width="1.2" fill="none"/></svg>
        quiet.morning.tide@mailpost.example
      </li>
    </ul>

    <p class="tagline">Tailored Calm Under Pressure Programs for managers and frontline service crews</p>
  </div>
</body>
</html>
```